Realtor branding business card

modern, simple and self branding. Broker office logo needs to be used but not emphasized. Looking to brand myself

Target Market(s)

buyers, sellers and investors

Industry/Entity Type

Realtor

Contact Information for Business Card

Sample of my current business card on file

Requirements
Must have
• my website - emilioverdaskt.com
• Realtor logo
• Fair housing logo
Nice to have
• Colors from office logo but not a must
Should not have
• Do not want headshot

```html
<!DOCTYPE html>
<html lang="en">
<head>
<meta charset="utf-8">
<title>Emilio Verdask – Realtor Business Card</title>
<link href="https://fonts.googleapis.com/css2?family=Roboto:wght@400;500;700;900&display=swap" rel="stylesheet">
<style>
  :root {
    --navy: #25215f;
    --red: #c8232a;
    --paper: #ececec;
    --ink: #3a3a3a;
    --backdrop: #2b2c2f;
    --white: #f4f4f4;
    --badge: #6b6b7a;
  }
  * { margin: 0; padding: 0; box-sizing: border-box; }
  html, body { width: 1200px; height: 1200px; overflow: hidden; }
  body {
    background: var(--backdrop);
    font-family: "Roboto", Arial, sans-serif;
    position: relative;
  }
  .card {
    position: absolute;
    left: 246px;
    width: 708px;
    height: 404px;
    overflow: hidden;
  }
  .card--front { top: 166px; background: var(--paper); }
  .card--back { top: 628px; background: var(--navy); }

  .brand {
    position: absolute;
    display: flex;
    flex-direction: column;
    align-items: flex-start;
    font-weight: 900;
    line-height: 0.95;
  }
  .brand__mark {
    width: 18px; height: 18px;
    background: var(--red);
    margin-bottom: 8px;
  }
  .brand__name { font-size: 40px; letter-spacing: -1px; }
  .brand__tag { font-size: 20px; letter-spacing: 1px; margin-top: 4px; }

  .card--front .brand { left: 63px; top: 140px; color: var(--navy); }

  .credentials {
    position: absolute;
    left: 63px; top: 262px;
    display: flex; gap: 12px; align-items: center;
  }
  .credentials__badge { width: 30px; height: 30px; background: var(--badge); }
  .credentials__badge--round { border-radius: 50%; }

  .divider {
    position: absolute;
    left: 354px; top: 112px;
    width: 1px; height: 180px;
    background: #8a8a8a;
  }
  .contact { position: absolute; left: 408px; top: 110px; color: var(--ink); }
  .contact__name { font-size: 26px; font-weight: 700; color: var(--navy); line-height: 1.1; }
  .contact__role { font-size: 16px; line-height: 1.3; }
  .contact__address { margin-top: 20px; font-size: 16px; line-height: 1.3; }
  .contact__lines { margin-top: 14px; list-style: none; font-size: 16.5px; line-height: 1.27; }
  .contact__lines li { display: flex; align-items: center; gap: 10px; }
  .contact__lines svg { width: 13px; height: 13px; fill: var(--navy); flex: none; }

  .swoosh { position: absolute; left: 0; bottom: 0; width: 708px; height: 404px; }
  .site {
    position: absolute;
    color: var(--white);
    font-size: 16px;
    letter-spacing: 2px;
    font-weight: 400;
    white-space: nowrap;
  }
  .site b { font-weight: 700; }
  .card--front .site { left: 405px; top: 373px; }

  .stars-field {
    position: absolute; right: 0; top: 0;
    width: 340px; height: 250px;
    background: radial-gradient(ellipse at 75% 30%, rgba(80,80,170,0.55), rgba(37,33,95,0) 70%);
  }
  .card--back .brand { left: 182px; top: 128px; color: var(--white); }
  .card--back .brand__mark { width: 22px; height: 22px; margin-bottom: 10px; }
  .card--back .brand__name { font-size: 66px; }
  .card--back .brand__tag { font-size: 33px; }
  .card--back .site { left: 0; right: 0; text-align: center; top: 340px; }
</style>
</head>
<body>
  <section class="card card--front">
    <div class="brand">
      <span class="brand__mark"></span>
      <span class="brand__name">Brightway</span>
      <span class="brand__tag">Realty Group</span>
    </div>
    <div class="credentials">
      <span class="credentials__badge" role="img" aria-label="Realtor membership badge"></span>
      <span class="credentials__badge credentials__badge--round" role="img" aria-label="Equal housing opportunity badge"></span>
    </div>
    <div class="divider"></div>
    <div class="contact">
      <p class="contact__name">Emilio Verdask, Pa</p>
      <p class="contact__role">Realtor</p>
      <p class="contact__address">482 Lakeview Crest Dr.<br>Maple Springs, FL 32901</p>
      <ul class="contact__lines">
        <li><svg viewBox="0 0 24 24"><path d="M6.6 10.8a15 15 0 0 0 6.6 6.6l2.2-2.2a1 1 0 0 1 1-.25 11.4 11.4 0 0 0 3.6.57 1 1 0 0 1 1 1V20a1 1 0 0 1-1 1A17 17 0 0 1 3 4a1 1 0 0 1 1-1h3.5a1 1 0 0 1 1 1c0 1.25.2 2.45.57 3.57a1 1 0 0 1-.25 1z"/></svg>407-555-0148</li>
        <li><svg viewBox="0 0 24 24"><path d="M6 2h12v5H6zM3 8h18a1 1 0 0 1 1 1v8h-4v5H6v-5H2V9a1 1 0 0 1 1-1zm5 8v4h8v-4z"/></svg>407-555-0192</li>
        <li><svg viewBox="0 0 24 24"><path d="M2 5h20v14H2zm2 2v.5l8 5 8-5V7zm0 2.8V17h16V9.8l-8 5z"/></svg>Verdaskrealty@mail.com</li>
      </ul>
    </div>
    <svg class="swoosh" viewBox="0 0 708 404" preserveAspectRatio="none" aria-hidden="true">
      <path d="M0 404 C180 340 450 340 708 366 L708 404 Z" fill="var(--red)"/>
      <path d="M120 404 C300 360 520 356 708 372 L708 404 Z" fill="var(--navy)"/>
    </svg>
    <p class="site">www.<b>emilioverdaskt</b>.com</p>
  </section>

  <section class="card card--back">
    <div class="stars-field" role="img" aria-label="Faint scattered star decoration"></div>
    <div class="brand">
      <span class="brand__mark"></span>
      <span class="brand__name">Brightway</span>
      <span class="brand__tag">Realty Group</span>
    </div>
    <p class="site">www.<b>emilioverdaskt</b>.com</p>
  </section>
</body>
</html>
```